Wordpress Website for electrician

I'm looking for an easy to maintain website for my electrical contracting business. Need a professional and appealing site.
Im wanting a website where clients can come on and look at services we offer, case studies and advertise our services.
Colours I'm wanting to incorporate are green, white, black and grey
I'm wanting a big slide show on main page where I can place advertising etc.
Menu is to include home, services, our work, specials, energy efficiency and contact
My existing site is www.trelwirefix.com.au
Updates
looking for something with a similar layout to this website
Target Market(s)
Businesses
Industry/Entity Type
Electrician
Look and feel

```html
<!DOCTYPE html>
<html lang="en">
<head>
<meta charset="utf-8">
<title>trelwirefix – Electrical Contracting</title>
<link href="https://fonts.googleapis.com/css2?family=Oswald:wght@400;600;700&family=Tinos:wght@400;700&family=Satisfy&family=Kalam:wght@400&display=swap" rel="stylesheet">
<style>
:root{
  --green:#4fae1f;
  --green-light:#9ccf2a;
  --green-pale:#eef7dc;
  --green-text:#2f9a2a;
  --black:#121212;
  --nav:#1d1d1d;
  --grey:#4a4a4a;
  --text:#555;
  --white:#fff;
  --yellow:#ffd400;
}
*{box-sizing:border-box;margin:0;padding:0}
html,body{width:697px;height:1200px;overflow:hidden;background:var(--white)}
body{position:relative;font-family:"Tinos",serif;color:var(--text)}
.abs{position:absolute}

/* header */
.site-header{left:0;top:0;width:697px;height:60px;background:linear-gradient(#f7fbec,#dcefb8)}
.contact-label{left:86px;top:6px;font-family:"Kalam",cursive;font-size:20px;color:#333;line-height:1}
.contact-phone{left:86px;top:27px;font-family:"Oswald",sans-serif;font-weight:700;font-size:22px;color:var(--green-text);line-height:1}
.brand{left:262px;top:10px;display:flex;align-items:center;gap:7px;font-family:"Oswald",sans-serif;font-weight:600;font-size:26px;color:var(--green-text);line-height:1}
.brand-mark{width:18px;height:18px;border-radius:50%;background:var(--green-text)}
.social{top:34px;width:22px;height:22px;border-radius:4px;background:#7f8c95}

/* nav */
.main-nav{left:0;top:60px;width:697px;height:24px;background:var(--nav);border-bottom:3px solid var(--green)}
.nav-list,.footer-nav{list-style:none;position:absolute;left:0;top:0;width:697px;height:22px}
.nav-list li,.footer-nav li{position:absolute;top:0;transform:translateX(-50%);white-space:nowrap;font-family:"Satisfy",cursive;font-size:15px;line-height:22px}
.nav-list li{color:var(--green-light)}
.nav-list li.active{color:var(--white)}

/* hero */
.hero{left:0;top:87px;width:697px;height:205px;background:radial-gradient(ellipse at 65% 35%,#1a7fc0 0%,#0a3a66 30%,#020a14 70%);border-bottom:3px solid var(--green)}
.partner{left:108px;top:200px;display:flex;align-items:center;gap:6px;font-size:19px;color:var(--white);white-space:nowrap}
.partner-mark{width:14px;height:14px;background:var(--yellow)}
.hero-title{left:357px;top:200px;font-family:"Oswald",sans-serif;font-weight:700;font-size:38px;color:var(--white);letter-spacing:-1px;line-height:1;white-space:nowrap}
.hero-sub{left:139px;top:238px;font-size:31px;color:var(--green-text);line-height:1;white-space:nowrap}

/* content */
.section-title{font-size:13.5px;font-weight:400;color:#333;border-bottom:3px solid var(--green);width:312px;padding-bottom:3px;line-height:1;white-space:nowrap}
.section-title b{font-weight:400;color:var(--green-text)}
.copy{font-size:8.6px;line-height:21px;color:#666;white-space:nowrap}
.btn{font-family:"Oswald",sans-serif;font-weight:600;font-size:10px;color:var(--white);height:19px;line-height:19px;text-align:center;white-space:nowrap;box-shadow:1px 1px 2px rgba(0,0,0,.35)}
.btn-green{background:linear-gradient(#a8d63a,#6aa814)}
.btn-grey{background:linear-gradient(#5a5a5a,#2c2c2c)}

.promo{left:426px;top:312px;width:188px;height:86px}
.promo div{white-space:nowrap}
.promo-pack{left:8px;top:8px;width:48px;height:52px;background:linear-gradient(#8a5cc4,#c9c1dd);border-radius:2px}
.promo-title{left:58px;top:5px;font-family:"Oswald",sans-serif;font-weight:700;font-size:14px;color:var(--green-text);line-height:1}
.promo-note{left:88px;top:22px;font-family:"Oswald",sans-serif;font-size:8px;color:#333}
.promo-price{left:96px;top:36px;font-family:"Oswald",sans-serif;font-weight:700;font-size:30px;color:#7fc62b;line-height:1}
.promo-each{left:150px;top:42px;font-family:"Oswald",sans-serif;font-size:7px;color:#7fc62b}
.promo-cond{left:6px;top:66px;font-family:"Oswald",sans-serif;font-size:6px;color:#333}
.promo-link{left:74px;top:72px;font-family:"Oswald",sans-serif;font-size:8px;color:#f2a400}

.news{left:415px;top:408px;width:200px;height:188px;background:var(--green-pale);border:1px solid #c9e0a2}
.news-title{left:6px;top:3px;font-size:13px;color:#555}
.news-item{left:10px;width:180px;font-size:6.5px;line-height:8px;color:#555}
.news-item .date{font-weight:700;display:block;margin-bottom:2px}
.news-item .more{font-weight:700;display:block;margin-top:1px}

/* dark services area */
.services{left:0;top:610px;width:697px;height:488px;background:linear-gradient(90deg,#161616,#2a2a2a 20%,#141414 40%,#262626 60%,#121212 80%,#222)}
.tile{width:214px;height:92px;color:var(--white)}
.tile h3{position:absolute;left:12px;top:12px;font-family:"Oswald",sans-serif;font-weight:600;font-size:11px;letter-spacing:.3px;white-space:nowrap}
.tile p{position:absolute;font-size:8.5px;line-height:12px}
.tile .read{position:absolute;right:8px;bottom:6px;background:var(--white);color:#111;font-size:6px;font-weight:700;padding:2px 6px;white-space:nowrap}
.tile-icon{position:absolute;left:12px;top:38px;width:30px;height:30px;background:#555;border-radius:3px}
.t-green{background:linear-gradient(#b4d62b,#6ba514)}
.t-blue{background:linear-gradient(#38c8f0,#1491c5)}
.t-grey{background:linear-gradient(#d2d2d2,#9a9a9a)}
.t-yellow{background:linear-gradient(#ffe400,#ff9500)}
.go-green{left:372px;top:716px;font-family:"Oswald",sans-serif;font-weight:700;font-size:26px;color:#1e3a14;letter-spacing:2px;white-space:nowrap}
.tree{left:540px;top:614px;width:112px;height:156px;background:radial-gradient(ellipse at 50% 40%,#4c6a2e,#1b2614 70%,transparent 72%)}

.testimonials-title{left:98px;top:1024px;font-family:"Oswald",sans-serif;font-weight:600;font-size:11px;color:var(--green-light)}
.quote{width:208px;font-size:7px;line-height:12px;color:#ddd}
.quote b{color:var(--white)}
.pager{left:566px;font-family:"Oswald",sans-serif;font-size:8px;color:var(--green-light);letter-spacing:.5px;white-space:nowrap}

/* footer */
.site-footer{left:0;top:1098px;width:697px;height:102px;background:linear-gradient(#fafdf2,#e3f2c6)}
.footer-nav{top:10px}
.footer-nav li{color:var(--green-text);font-size:16px}
.footer-nav li.active{color:#444}
.footer-meta{left:0;width:697px;text-align:center;font-size:8px;color:#555;font-weight:700;letter-spacing:.4px}
.footer-phone{left:276px;top:1156px;width:156px;height:34px;background:linear-gradient(#a7d53c,#6aa814);border:2px solid #e3f2c6;box-shadow:0 0 3px rgba(0,0,0,.35);font-family:"Oswald",sans-serif;font-weight:700;font-size:22px;color:var(--white);text-align:center;line-height:30px}
</style>
</head>
<body>

<header class="abs site-header">
  <div class="abs contact-label">Contact Us:</div>
  <div class="abs contact-phone">0400 555 019</div>
  <div class="abs brand"><span class="brand-mark"></span>trelwirefix</div>
  <span class="abs social" style="left:494px"></span>
  <span class="abs social" style="left:532px"></span>
  <span class="abs social" style="left:584px"></span>
</header>

<nav class="abs main-nav">
  <ul class="nav-list">
    <li class="active" style="left:116px">Home</li>
    <li style="left:198px">About</li>
    <li style="left:286px">Services</li>
    <li style="left:385px">Our Work</li>
    <li style="left:486px">Specials</li>
    <li style="left:578px">Contact</li>
  </ul>
</nav>

<section class="abs hero" role="img" aria-label="Slideshow banner: glowing blue circuit lines and light bokeh on black"></section>
<div class="abs partner"><span class="partner-mark"></span>BrightLeaf Electricians</div>
<div class="abs hero-title">BOOK US TODAY</div>
<div class="abs hero-sub">SAVE ENERGY... SAVE MONEY</div>

<h2 class="abs section-title" style="left:86px;top:302px"><b>LED IS THE</b> FUTURE</h2>
<p class="abs copy" style="left:86px;top:320px">LED lighting has involved rapidly in the last 5 years. In the coming years we will see<br>all lighting being substituted with LED lights. It is by far the most efficient form of<br>lighting on todays market. Let us retrofit your business or home with LED and the<br>savings will literally pay the lights off.</p>
<div class="abs btn btn-green" style="left:250px;top:413px;width:56px">WHY LED?</div>
<div class="abs btn btn-grey" style="left:317px;top:413px;width:84px">REQUEST QUOTE</div>

<h2 class="abs section-title" style="left:86px;top:467px"><b>REDUCE YOUR BUSINESS ENERGY</b> CONSUMPTION</h2>
<p class="abs copy" style="left:86px;top:488px">LED lighting has involved rapidly in the last 5 years. In the coming years we will see<br>all lighting being substituted with LED lights. It is by far the most efficient form of<br>lighting on todays market. Let us retrofit your business or home with LED and the<br>savings will literally pay the lights off.</p>
<div class="abs btn btn-green" style="left:187px;top:577px;width:119px">ENERGY EFFICIENCY AUDIT</div>
<div class="abs btn btn-grey" style="left:317px;top:577px;width:84px">BOOK AUDIT</div>

<aside class="abs promo">
  <div class="abs promo-pack" role="img" aria-label="LED downlight product box"></div>
  <div class="abs promo-title">LED DOWNLIGHTS</div>
  <div class="abs promo-note">Supplied &amp; Installed</div>
  <div class="abs promo-price">$33</div>
  <div class="abs promo-each">EACH</div>
  <div class="abs promo-cond">CONDITIONS APPLY</div>
  <div class="abs promo-link">Click here for more details</div>
</aside>

<aside class="abs news">
  <div class="abs news-title">NEWS</div>
  <div class="abs news-item" style="top:20px"><span class="date">13.08.2013</span>New LED range now in stock. Call our team for a free lighting check today.<span class="more">read more...</span></div>
  <div class="abs news-item" style="top:72px"><span class="date">13.08.2013</span>New LED range now in stock. Call our team for a free lighting check today.<span class="more">read more...</span></div>
  <div class="abs news-item" style="top:124px"><span class="date">13.08.2013</span>New LED range now in stock. Call our team for a free lighting check today.<span class="more">read more...</span></div>
  <div class="abs btn btn-green" style="left:120px;top:165px;width:68px">READ ALL</div>
</aside>

<section class="abs services"></section>
<div class="abs tree" role="img" aria-label="Glowing green tree illustration"></div>
<div class="abs go-green">GO GREEN</div>

<article class="abs tile t-green" style="left:86px;top:612px">
  <h3>ELECTRICAL CONTRACTING</h3><span class="tile-icon"></span>
  <p style="left:54px;top:42px;width:150px">We offer all types of electrical work from Installation to maintenance</p>
  <span class="read">READ MORE</span>
</article>
<article class="abs tile t-blue" style="left:336px;top:612px">
  <h3>ENERGY EFFICIENCY</h3>
  <svg class="abs" style="left:12px;top:40px" width="30" height="30" viewBox="0 0 30 30"><circle cx="15" cy="13" r="8" fill="#ffd400"/><rect x="11" y="21" width="8" height="5" fill="#333"/></svg>
  <p style="left:54px;top:32px;width:150px">With one of our audits to your business or home we can lower your energy bills and minimise your carbon footprint</p>
  <span class="read">READ MORE</span>
</article>
<article class="abs tile t-grey" style="left:86px;top:770px">
  <h3>UNDERGROUND LOCATING</h3><span class="tile-icon"></span>
  <p style="left:54px;top:42px;width:150px;color:#222">We have the tools and knowledge in locating underground utilities.</p>
  <span class="read">READ MORE</span>
</article>
<article class="abs tile t-yellow" style="left:336px;top:770px">
  <h3>NEWS</h3>
  <p style="left:12px;top:32px;width:195px;color:#222">ELECTRICITY PRICES TO SOAR<br>The Australian government's carbon tax will see electricity prices soar</p>
  <span class="read">READ MORE</span>
</article>
<article class="abs tile t-blue" style="left:86px;top:896px">
  <h3>SPECIALS</h3>
  <p style="left:12px;top:36px;width:195px;color:#111">COOLWAVE SPLIT SYSTEM<br>Beat the heat this summer! We can supply and install a new split system....</p>
  <span class="read">READ MORE</span>
</article>
<article class="abs tile t-green" style="left:336px;top:896px">
  <h3>SPECIALS</h3>
  <p style="left:12px;top:36px;width:195px;color:#111">COOLWAVE SPLIT SYSTEM<br>Beat the heat this summer! We can supply and install a new split system....</p>
  <span class="read">READ MORE</span>
</article>

<div class="abs testimonials-title">TESTIMONIALS</div>
<p class="abs quote" style="left:98px;top:1044px">Phasellus scelerisque nec orci suscipit congue. Mauris et metus quis lacus luctus semper. Nunc aliquet erat id convallis hendrerit. Donec id est vitae lectus dictum bibendum. Phasellus ultrices porttitor...<br><b>read more</b></p>
<p class="abs quote" style="left:336px;top:1044px">Phasellus scelerisque nec orci suscipit congue. Mauris et metus quis lacus luctus semper. Nunc aliquet erat id convallis hendrerit. Donec id est vitae lectus dictum bibendum. Phasellus ultrices porttitor...<br><b>read more</b></p>
<div class="abs pager" style="top:1050px">&lsaquo;&nbsp; PREVIOUS</div>
<div class="abs pager" style="top:1074px">&rsaquo;&nbsp; NEXT</div>

<footer class="abs site-footer">
  <ul class="footer-nav">
    <li class="active" style="left:116px">Home</li>
    <li style="left:198px">About</li>
    <li style="left:286px">Services</li>
    <li style="left:385px">Our Work</li>
    <li style="left:486px">Specials</li>
    <li style="left:578px">Contact</li>
  </ul>
</footer>
<div class="abs footer-meta" style="top:1131px">sales@trelwirefix.com</div>
<div class="abs footer-meta" style="top:1143px">PROUDLY ACCREDITED BRIGHTLEAF ELECTRICIANS</div>
<div class="abs footer-phone">0400 555 019</div>

</body>
</html>
```